KELU Nature Soap

We need to design new product Nature and medicative Soap.Made in Malaysia
* 100% natural.
* made from nature Tropic oil.
* Very effective for Acne & Skin irritation
* size 100 Gm.
* Use for all skin types including sensitive skin
* Name of the product " KELU Soap"

Reason: please I need to extended since I haven't receive any suitable design for my project

Target Market(s)

International

Industry/Entity Type

Hair And Beauty

Font styles to use
Serif

Colors
33a6d7
abd037
fbed22

Requirements
Must have
• * must have English- Arabic ingredient
• * Very effective for Acne & Skin irritation
Nice to have
• * some things related to natural (water,tree,face..)
• * Show faces picture (after - before)

```html
<!DOCTYPE html>
<html lang="en">
<head>
<meta charset="utf-8">
<title>KELU Soap – Tube Label</title>
<link rel="stylesheet" href="https://fonts.googleapis.com/css2?family=Marcellus&display=swap">
<style>
  :root {
    --bg: #e4e9ec;
    --leaf-dark: #2f6b2a;
    --leaf-mid: #abd037;
    --leaf-light: #e6eca0;
    --seal: #fbed22;
    --text-light: #ffffff;
    --shadow: rgba(20, 40, 20, 0.45);
  }
  * { margin: 0; padding: 0; box-sizing: border-box; }
  html, body { width: 1200px; height: 848px; overflow: hidden; }
  body {
    background: var(--bg);
    font-family: "Marcellus", serif;
    position: relative;
  }
  .label {
    position: absolute;
    top: 130px;
    width: 340px;
    height: 580px;
    overflow: hidden;
  }
  .label--front { left: 240px; }
  .label--back  { left: 620px; }
  .label__seal {
    height: 18px;
    background: var(--seal);
  }
  .label__pattern {
    position: absolute;
    top: 18px; left: 0; right: 0; bottom: 0;
    background:
      repeating-linear-gradient(160deg, rgba(47,107,42,0.55) 0 3px, transparent 3px 22px),
      linear-gradient(165deg, var(--leaf-light) 0%, var(--leaf-mid) 45%, #8fb02c 70%, var(--leaf-mid) 100%);
  }
  .label__content {
    position: absolute;
    top: 18px; left: 0; right: 0; bottom: 0;
    color: var(--text-light);
    text-shadow: 0 2px 4px var(--shadow);
  }
  .brand-mark {
    position: absolute;
    top: 60px; left: 0; right: 0;
    display: flex;
    align-items: center;
    justify-content: center;
    gap: 8px;
    font-size: 24px;
    letter-spacing: 2px;
  }
  .brand-mark__dot {
    width: 14px; height: 14px;
    border-radius: 50%;
    background: var(--text-light);
  }
  .product-name {
    position: absolute;
    top: 190px; left: 0; right: 0;
    text-align: center;
    line-height: 0.95;
  }
  .product-name__brand { display: block; font-size: 74px; letter-spacing: 1px; }
  .product-name__type  { display: block; font-size: 62px; }
  .product-size {
    position: absolute;
    top: 410px; left: 0; right: 0;
    text-align: center;
    font-size: 22px;
  }
  .product-origin {
    position: absolute;
    top: 485px; left: 0; right: 0;
    text-align: center;
    font-size: 16px;
  }
  .benefits {
    list-style: none;
    position: absolute;
    top: 90px; left: 36px; right: 30px;
    font-size: 17px;
    line-height: 2.2;
  }
</style>
</head>
<body>
  <section class="label label--front">
    <div class="label__seal"></div>
    <div class="label__pattern" role="img" aria-label="Flowing green and yellow leaf wave pattern"></div>
    <div class="label__content">
      <div class="brand-mark"><span class="brand-mark__dot"></span><span>KELU</span></div>
      <h1 class="product-name">
        <span class="product-name__brand">KELU</span>
        <span class="product-name__type">Soap</span>
      </h1>
      <p class="product-size">100 Gm</p>
      <p class="product-origin">Made in Malaysia</p>
    </div>
  </section>

  <section class="label label--back">
    <div class="label__seal"></div>
    <div class="label__pattern" role="img" aria-label="Flowing green and yellow leaf wave pattern"></div>
    <div class="label__content">
      <ul class="benefits">
        <li>Made from nature Tropic oil.</li>
        <li>Very effective for</li>
        <li>Acne &amp; Skin irritation</li>
        <li>Use for all skin types</li>
        <li>including sensitive skin</li>
      </ul>
    </div>
  </section>
</body>
</html>
```